Wavelume artwork for new single release

I need Wavelume artwork creating to release a new single on there.

The specs are:

Ideal size: 3000 x 3000 pixels
Minimum size: 1400 x 1400 pixels
Aspect ratio: 1:1 (must be a perfect square)
File format: JPG or PNG
Color space: sRGB
File size: Max 4MB

The song is called "Still, Can We Wander?"
The artist is "Milo Fenwright"

We have no images of Milo, so it really is open to imagination.

Target Market(s)

Wavelume listeners

Industry/Entity Type

Music

```html
<!DOCTYPE html>
<html lang="en">
<head>
<meta charset="UTF-8">
<title>Still, Can We Wander? — Milo Fenwright</title>
<link href="https://fonts.googleapis.com/css2?family=Montserrat:wght@500;700&display=swap" rel="stylesheet">
<style>
  :root {
    --backdrop: #e6e6e6;
    --card: #ffffff;
    --ink: #000000;
    --heart: #e3202b;
    --art-magenta: #eb0a6c;
    --art-plum: #7c3e70;
    --art-slate: #3a5462;
    --art-teal: #2f4b58;
  }
  * { margin: 0; padding: 0; box-sizing: border-box; }
  html, body {
    width: 1200px;
    height: 2400px;
    overflow: hidden;
    background: var(--backdrop);
    font-family: "Montserrat", Arial, sans-serif;
  }
  .canvas {
    position: relative;
    width: 1200px;
    height: 2400px;
  }
  .showcase {
    position: absolute;
    left: 0; top: 0;
    width: 1200px;
    height: 1200px;
    background: var(--backdrop);
  }
  .player-card {
    position: absolute;
    left: 260px; top: 132px;
    width: 680px;
    height: 937px;
    background: var(--card);
  }
  .cover-art {
    position: absolute;
    left: 64px; top: 66px;
    width: 552px;
    height: 552px;
  }
  .artwork-fill {
    background: linear-gradient(90deg,
      var(--art-magenta) 0%,
      #c81a6c 12%,
      var(--art-plum) 32%,
      #5a4a68 44%,
      var(--art-slate) 56%,
      var(--art-teal) 100%);
  }
  .track-title {
    position: absolute;
    left: 66px; top: 642px;
    font-weight: 700;
    font-size: 30px;
    letter-spacing: 0.5px;
    color: var(--ink);
    line-height: 1;
  }
  .track-artist {
    position: absolute;
    left: 67px; top: 680px;
    font-weight: 500;
    font-size: 23px;
    letter-spacing: 0.4px;
    color: var(--ink);
    line-height: 1;
  }
  .like-icon {
    position: absolute;
    left: 576px; top: 670px;
    width: 34px; height: 30px;
  }
  .progress {
    position: absolute;
    left: 64px; top: 742px;
    width: 552px; height: 20px;
  }
  .controls {
    position: absolute;
    left: 0; top: 780px;
    width: 680px; height: 124px;
  }
  .art-detail {
    position: absolute;
    left: 0; top: 1200px;
    width: 1200px;
    height: 1200px;
  }
</style>
</head>
<body>
<main class="canvas">
  <section class="showcase">
    <article class="player-card">
      <div class="cover-art artwork-fill" role="img" aria-label="Grainy halftone portrait of the artist in profile, fading from magenta on the left to dark teal on the right"></div>

      <h1 class="track-title">Still, Can We Wander?</h1>
      <p class="track-artist">Milo Fenwright</p>

      <svg class="like-icon" viewBox="0 0 34 30" aria-label="Liked">
        <path d="M17 29 C6 20 1 15 1 9 C1 4 5 1 9.5 1 C13 1 15.5 3 17 6 C18.5 3 21 1 24.5 1 C29 1 33 4 33 9 C33 15 28 20 17 29 Z" fill="var(--heart)"/>
      </svg>

      <svg class="progress" viewBox="0 0 552 20" aria-label="Playback position">
        <line x1="1" y1="10" x2="551" y2="10" stroke="var(--ink)" stroke-width="3.5" stroke-linecap="round"/>
        <circle cx="276" cy="10" r="10" fill="var(--ink)"/>
      </svg>

      <svg class="controls" viewBox="0 0 680 124" aria-label="Playback controls">
        <g class="shuffle" fill="none" stroke="var(--ink)" stroke-width="3.5" stroke-linecap="round" stroke-linejoin="round">
          <path d="M58 49 C75 49 80 75 104 75 L115 75"/>
          <path d="M58 75 C75 75 80 49 104 49 L115 49"/>
          <path d="M108 42 L116 49 L108 56"/>
          <path d="M108 68 L116 75 L108 82"/>
        </g>
        <g class="previous" fill="var(--ink)">
          <rect x="177" y="43" width="5" height="40"/>
          <path d="M214 43 L214 83 L182 63 Z"/>
        </g>
        <g class="play">
          <circle cx="340" cy="62" r="50" fill="none" stroke="var(--ink)" stroke-width="4"/>
          <path d="M324 43 L324 81 L357 62 Z" fill="var(--ink)"/>
        </g>
        <g class="next" fill="var(--ink)">
          <path d="M466 43 L466 83 L498 63 Z"/>
          <rect x="497" y="43" width="5" height="40"/>
        </g>
        <g class="repeat" fill="none" stroke="var(--ink)" stroke-width="3.5" stroke-linecap="round" stroke-linejoin="round">
          <path d="M576 66 L576 56 C576 50 580 47 586 47 L620 47"/>
          <path d="M613 40 L621 47 L613 54"/>
          <path d="M621 58 L621 68 C621 74 617 77 611 77 L577 77"/>
          <path d="M584 70 L576 77 L584 84"/>
        </g>
      </svg>
    </article>
  </section>

  <section class="art-detail artwork-fill" role="img" aria-label="Close-up of the cover artwork: grainy halftone portrait in profile, magenta fading into dark teal"></section>
</main>
</body>
</html>
```